PowerPoint template for a tech startup

We need a PowerPoint template with a title slide, text slide, section slide, and thank you slide.
Our application helps engineering teams to be more productive. We would love a design that is slick, sophisticated, and consistent with our brand. (see more at www.quenvomi.io or attached files)
By the way (not a requirement), Quenvo means lighthouse in Greek.
Also, here is the font we used (not required) - https://fonts.trelvanic.com/fonts/league-gothic

Other font styles liked:
• https://fonts.trelvanic.com/fonts/league-gothic

```html
<!DOCTYPE html>
<html lang="en">
<head>
<meta charset="utf-8">
<title>Quenvo — Presentation Template</title>
<link href="https://fonts.googleapis.com/css2?family=Nunito+Sans:wght@700;800;900&family=Carlito:wght@400;700&display=swap" rel="stylesheet">
<style>
:root{
  --board:#435356;
  --brand:#1716e6;
  --brand-deep:#1a12d8;
  --brand-bright:#2a4dff;
  --ink-blue:#1414e2;
  --white:#ffffff;
  --paper:#ffffff;
  --faint-on-blue:rgba(255,255,255,.28);
  --faint-on-white:rgba(20,20,226,.22);
  --placeholder:#8d91f4;
}
*{margin:0;padding:0;box-sizing:border-box}
html,body{width:1200px;height:849px;overflow:hidden;background:var(--board)}
body{position:relative;font-family:"Carlito",sans-serif}
.slide{position:absolute;width:365px;height:258px;overflow:hidden;box-shadow:3px 4px 8px rgba(0,0,0,.45)}
.slide--blue{background:linear-gradient(200deg,var(--brand-bright) 0%,var(--brand) 45%,var(--brand-deep) 100%);color:var(--white)}
.slide--white{background:radial-gradient(ellipse at 20% 30%,#f4f5fb 0%,var(--paper) 60%);color:var(--ink-blue)}
.abs{position:absolute}
.heading{font-family:"Nunito Sans",sans-serif;font-weight:900;letter-spacing:-.1px}
.brand-name{position:absolute;font-family:"Nunito Sans",sans-serif;font-weight:800;font-size:17px;line-height:1;color:var(--white)}
.rule{position:absolute;width:1.5px;height:43px}
.rule--white{background:var(--white)}
.rule--blue{background:var(--ink-blue)}
.vlabel{position:absolute;writing-mode:vertical-rl;font-family:"Nunito Sans",sans-serif;font-weight:700;font-size:5px;letter-spacing:.6px;white-space:nowrap}
.vlabel--faint-blue{color:var(--faint-on-blue)}
.vlabel--faint-white{color:var(--faint-on-white)}
.vlabel--site{font-size:5.5px;letter-spacing:.3px}
.copyright{position:absolute;top:232px;font-size:4px;white-space:nowrap}
.page-no{position:absolute;top:229px;left:336px;font-family:"Nunito Sans",sans-serif;font-weight:700;font-size:7px}
.site{position:absolute;font-family:"Nunito Sans",sans-serif;font-weight:700;font-size:6.5px;letter-spacing:.4px}
/* title slide */
.title-main{left:48px;top:87px;font-size:20px;line-height:21px}
.title-lede{left:48px;top:171px;width:280px;font-size:5.8px;line-height:6.5px;font-weight:700}
/* contents slide */
.contents-head{left:58px;top:35px;font-size:13px}
.contents-row{position:absolute;left:60px;width:240px;display:flex}
.contents-row__label{width:68px;font-family:"Nunito Sans",sans-serif;font-weight:900;font-size:7px}
.contents-row__text{width:170px;font-size:5.8px;line-height:6.9px;font-weight:700;text-align:justify}
/* text slide */
.side-panel{position:absolute;left:0;top:0;width:110px;height:258px;background:linear-gradient(200deg,var(--brand-bright),var(--brand) 50%,var(--brand-deep))}
.image-slot{position:absolute;left:28px;top:112px;width:63px;height:69px;background:var(--placeholder)}
.image-caption{position:absolute;left:28px;top:191px;width:68px;font-size:2.4px;line-height:3.3px;color:var(--white);text-align:justify}
.block-title{font-size:13px;line-height:14px}
.subhead{font-size:5.8px;font-weight:700}
.body-copy{font-size:4.3px;line-height:6.9px;text-align:justify}
/* section slide */
.section-band{position:absolute;left:0;top:0;width:365px;height:110px;background:linear-gradient(200deg,var(--brand-bright),var(--brand) 50%,var(--brand-deep))}
.column{position:absolute;top:122px;width:85px;color:var(--ink-blue)}
.column__head{font-family:"Nunito Sans",sans-serif;font-weight:800;font-size:5.5px;margin-bottom:3px}
.column__body{font-size:4.3px;line-height:6.9px;text-align:justify;height:78px}
.column__button{display:inline-block;margin-top:4px;background:var(--ink-blue);color:var(--white);font-family:"Nunito Sans",sans-serif;font-weight:800;font-size:4px;width:58px;height:10px;line-height:10px;text-align:center}
/* closing slide */
.thanks{left:0;width:365px;top:94px;text-align:center;font-size:20px}
.thanks-sub{left:0;width:365px;top:150px;text-align:center;font-size:6px;font-weight:700}
</style>
</head>
<body>

<!-- Title slide -->
<section class="slide slide--blue" style="left:31px;top:141px">
  <div class="rule rule--white" style="left:35px;top:38px"></div>
  <div class="site" style="left:48px;top:36px">www.quenvomi.io</div>
  <div class="brand-name" style="left:278px;top:44px">Quenvo</div>
  <div class="vlabel vlabel--faint-blue" style="left:15px;top:91px">TITLE SLIDE / TAGLINE</div>
  <h1 class="abs heading title-main">The Connected<br>Engineering Operations<br>Platform</h1>
  <p class="abs title-lede">Lorem ipsum dolor sit amet consectetuer odio non tellus natoque accumsan. Sed hac enim Lorem tempus tortor justo eget scelerisque sed morbi.</p>
  <div class="copyright" style="left:161px">© 2022, QUENVO AI, Inc.</div>
</section>

<!-- Contents slide -->
<section class="slide slide--white" style="left:418px;top:141px">
  <div class="vlabel vlabel--faint-white" style="left:27px;top:104px">SECTION SLIDE</div>
  <h2 class="abs heading contents-head">CONTENT</h2>
  <div class="rule rule--blue" style="left:335px;top:38px"></div>
  <div class="vlabel vlabel--site" style="left:350px;top:134px;color:var(--ink-blue)">www.quenvomi.io</div>
  <div class="contents-row" style="top:68px"><div class="contents-row__label">Lorem ipsum</div><p class="contents-row__text">Lorem ipsum dolor sit amet consectetuer odio non tellus natoque accumsan. Sed hac enim Lorem tempus tortor justo eget scelerisque sed morbi. Senectus urna Vestibulum tinci­dunt turpis sem magna Nam hendrerit vitae nibh.</p></div>
  <div class="contents-row" style="top:106px"><div class="contents-row__label">Lorem ipsum</div><p class="contents-row__text">Lorem ipsum dolor sit amet consectetuer odio non tellus natoque accumsan. Sed hac enim Lorem tempus tortor justo eget scelerisque sed morbi. Senectus urna Vestibulum tinci­dunt turpis sem magna Nam hendrerit vitae nibh.</p></div>
  <div class="contents-row" style="top:143px"><div class="contents-row__label">Lorem ipsum</div><p class="contents-row__text">Lorem ipsum dolor sit amet consectetuer odio non tellus natoque accumsan. Sed hac enim Lorem tempus tortor justo eget scelerisque sed morbi. Senectus urna Vestibulum tinci­dunt turpis sem magna Nam hendrerit vitae nibh.</p></div>
  <div class="contents-row" style="top:182px"><div class="contents-row__label">Lorem ipsum</div><p class="contents-row__text">Lorem ipsum dolor sit amet consectetuer odio non tellus natoque accumsan. Sed hac enim Lorem tempus tortor justo eget scelerisque sed morbi. Senectus urna Vestibulum tinci­dunt turpis sem magna Nam hendrerit vitae nibh.</p></div>
  <div class="copyright" style="left:161px">© 2022, QUENVO AI, Inc.</div>
  <div class="page-no">.1</div>
</section>

<!-- Text slide -->
<section class="slide slide--white" style="left:804px;top:141px">
  <div class="side-panel"></div>
  <div class="brand-name" style="left:28px;top:44px">Quenvo</div>
  <div class="vlabel vlabel--site" style="left:9px;top:134px;color:var(--white)">www.quenvomi.io</div>
  <div class="image-slot" role="img" aria-label="Product screenshot or supporting image"></div>
  <p class="image-caption">Get operational data and insights from your entire engineering organization. <b>Quenvo</b> gives leaders unprecedented visibility into engineering operations.</p>
  <div class="vlabel vlabel--faint-white" style="left:118px;top:110px">TEXT SLIDE</div>
  <h2 class="abs heading block-title" style="left:138px;top:36px">The Connected<br>Engineering Operations<br>Platform</h2>
  <div class="rule rule--blue" style="left:337px;top:38px"></div>
  <p class="abs subhead" style="left:138px;top:92px">Lorem ipsum dolor sit amet consectetuer odio</p>
  <p class="abs body-copy" style="left:138px;top:109px;width:200px">Lorem ipsum dolor sit amet consectetuer odio non tellus natoque accumsan. Sed hac enim Lorem tempus tortor justo eget scelerisque sed morbi. Senectus urna Vestibulum tincidunt turpis sem magna Nam hendrerit vitae nibh. Auctor Sed urna dignissim malesuada eleifend ultrices justo Curabitur Maecenas orci. Tincidunt adipiscing elit et et ac tincidunt elit nulla mauris eleifend. Urna. Quis ante odio consectetuer interdum eu dolor natoque Nam libero mollis. Euismod lacus ut velit tellus malesuada velit Curabitur quis semper a.</p>
  <p class="abs body-copy" style="left:138px;top:157px;width:200px">Egestas eros quis sapien eu nunc Pellentesque Nulla Aenean congue magna. Nibh felis Morbi id iaculis tellus laoreet molestie Curabitur lorem Proin. Elit consequat cursus lorem eu In leo in diam tortor elit. Justo. Penatibus lacus leo elit semper tempor arcu facilisis tincidunt nulla enim. Dolor semper pretium sem pellentesque senectus sem fames lacinia sagittis elit. Nam Nulla Quisque sagittis et turpis Donec justo eu In Lorem. Lacinia id semper id dictum malesuada dui Integer platea lorem Morbi. Neque Ut mauris ut ut urna dolor fringilla pharetra eget magna.</p>
  <div class="copyright" style="left:162px">© 2022, QUENVO AI, Inc.</div>
  <div class="page-no">.2</div>
</section>

<!-- Section slide -->
<section class="slide slide--white" style="left:225px;top:446px">
  <div class="section-band"></div>
  <div class="brand-name" style="left:29px;top:43px">Quenvo</div>
  <h2 class="abs heading block-title" style="left:136px;top:35px;color:var(--white)">The Connected<br>Engineering Operations<br>Platform</h2>
  <div class="rule rule--white" style="left:335px;top:37px;height:45px"></div>
  <p class="abs subhead" style="left:136px;top:92px;color:var(--white)">Lorem ipsum dolor sit amet consectetuer odio</p>
  <div class="vlabel vlabel--site" style="left:9px;top:134px;color:var(--ink-blue)">www.quenvomi.io</div>
  <div class="column" style="left:43px">
    <h3 class="column__head">LOREM IPSUM DOLOR SIT</h3>
    <p class="column__body">Lorem ipsum dolor sit amet consectetuer odio non tellus natoque accumsan. Sed hac enim Lorem tempus tortor justo eget scelerisque sed morbi. Senectus urna Vestibulum tincidunt turpis sem magna Nam hendrerit vitae nibh. Auctor Sed urna dignissim malesuada eleifend ultrices justo Curabitur Maecenas orci. Tincidunt adipiscing elit et et ac tinci­dunt elit nulla mauris eleifend.</p>
    <span class="column__button">Lorem ipsum dolor sit</span>
  </div>
  <div class="column" style="left:148px">
    <h3 class="column__head">LOREM IPSUM DOLOR SIT</h3>
    <p class="column__body">Lorem ipsum dolor sit amet consectetuer odio non tellus natoque accumsan. Sed hac enim Lorem tempus tortor justo eget scelerisque sed morbi. Senectus urna Vestibulum tincidunt turpis sem magna Nam hendrerit vitae nibh. Auctor Sed urna dignissim malesuada eleifend ultrices justo Curabitur Maecenas orci. Tincidunt adipiscing elit et et ac tinci­dunt elit nulla mauris eleifend.</p>
    <span class="column__button">Lorem ipsum dolor sit</span>
  </div>
  <div class="column" style="left:253px">
    <h3 class="column__head">LOREM IPSUM DOLOR SIT</h3>
    <p class="column__body">Lorem ipsum dolor sit amet consectetuer odio non tellus natoque accumsan. Sed hac enim Lorem tempus tortor justo eget scelerisque sed morbi. Senectus urna Vestibulum tincidunt turpis sem magna Nam hendrerit vitae nibh. Auctor Sed urna dignissim malesuada eleifend ultrices justo Curabitur Maecenas orci. Tincidunt adipiscing elit et et ac tinci­dunt elit nulla mauris eleifend.</p>
    <span class="column__button">Lorem ipsum dolor sit</span>
  </div>
  <div class="copyright" style="left:161px">© 2022, QUENVO AI, Inc.</div>
  <div class="page-no">.3</div>
</section>

<!-- Closing slide -->
<section class="slide slide--blue" style="left:611px;top:446px">
  <div class="vlabel vlabel--faint-blue" style="left:15px;top:97px">THANK YOU SLIDE</div>
  <h2 class="abs heading thanks">THANK YOU</h2>
  <p class="abs thanks-sub">Lorem ipsum dolor sit amet</p>
  <div class="copyright" style="left:0;width:365px;text-align:center">© 2022, QUENVO AI, Inc.</div>
</section>

</body>
</html>
```